Single Webpage Custom Design

We need a single page for a service-offering on http://awareness.tovenquard.com/. I created a draft so you can see what content should be on that page.

```html
<!DOCTYPE html>
<html lang="en">
<head>
<meta charset="utf-8">
<title>Awareness Training – Build Your Course</title>
<link href="https://fonts.googleapis.com/css2?family=Montserrat:wght@400;500;600;700&family=Roboto:wght@400;500;700&display=swap" rel="stylesheet">
<style>
:root{
  --page:#dfe3e7;
  --card:#ffffff;
  --navy:#0e2e45;
  --navy-2:#16425e;
  --teal:#17b1c2;
  --teal-dark:#0f8f9c;
  --footer:#00b3bb;
  --ink:#1d1d1f;
  --line:#dcdfe3;
  --orange-1:#f0ad43;
  --orange-2:#c97e12;
  --grey-1:#c4c4c4;
  --grey-2:#8f8f8f;
  --button:#0c3d73;
}
*{margin:0;padding:0;box-sizing:border-box}
html,body{width:1200px;height:4167px;overflow:hidden}
body{position:relative;background:var(--page);font-family:"Roboto",Arial,sans-serif;color:var(--ink)}
.abs{position:absolute}
.card{position:absolute;left:120px;width:960px;background:var(--card);box-shadow:0 2px 6px rgba(0,0,0,.05)}
.band{position:absolute;left:0;top:0;width:960px;background:linear-gradient(100deg,var(--navy) 0%,var(--navy-2) 60%,var(--navy) 100%)}
.badge{position:absolute;width:155px;height:138px;border-radius:14px;color:#fff;font-family:"Montserrat",sans-serif;text-align:center;padding-top:26px;box-shadow:0 3px 6px rgba(0,0,0,.2)}
.badge .step{font-size:34px;font-weight:400;letter-spacing:1px;line-height:40px}
.badge .num{font-size:34px;font-weight:700;line-height:50px}
.badge.orange{background:linear-gradient(180deg,var(--orange-1),var(--orange-2))}
.badge.teal{background:linear-gradient(180deg,#2cc0c8,var(--teal-dark))}
.badge.grey{background:linear-gradient(180deg,var(--grey-1),var(--grey-2))}
.band-title{position:absolute;font-family:"Montserrat",sans-serif;font-weight:600;font-size:28px;color:var(--teal);letter-spacing:.5px}
.band-sub{position:absolute;font-family:"Montserrat",sans-serif;font-weight:500;font-size:19px;color:#fff;line-height:24px;letter-spacing:.5px}
.body-text{position:absolute;font-size:13px;line-height:18px;color:var(--ink)}
.sec-title{position:absolute;font-family:"Montserrat",sans-serif;font-weight:700;font-size:19px;color:var(--teal);letter-spacing:.6px}
.type-card{position:absolute;top:391px;width:226px;height:188px;background:#fff;border-radius:4px;box-shadow:0 1px 4px rgba(0,0,0,.08);text-align:center}
.type-card.raised{box-shadow:0 2px 10px rgba(0,0,0,.14)}
.type-card h3{font-size:13.5px;font-weight:700;margin-top:28px;letter-spacing:.2px}
.type-visual{width:156px;height:104px;margin:16px auto 0;border-radius:50px;background:linear-gradient(180deg,#eef7fc 0%,#d9eef8 100%)}
.topic-list{position:absolute;top:605px;width:226px;height:452px;border:1.5px solid var(--line);border-radius:5px;list-style:none;padding:18px 0 0 28px}
.topic-list li{font-size:13.5px;font-weight:700;line-height:27.5px;position:relative;padding-left:2px}
.topic-list li::before{content:"";position:absolute;left:-14px;top:11px;width:7px;height:7px;border-radius:50%;background:var(--teal)}
.photo{position:absolute;left:572px;width:388px;height:257px}
.download{position:absolute;left:661px;top:70px;width:238px;height:91px;background:var(--button);border-radius:4px;color:#fff;font-family:"Montserrat",sans-serif;font-size:21px;font-weight:500;display:flex;align-items:center;padding-left:36px;gap:26px}
.footer{position:absolute;left:0;top:3716px;width:1200px;height:451px;background:var(--footer);color:#fff}
.f-title{position:absolute;font-family:"Montserrat",sans-serif;font-weight:500;font-size:27px;letter-spacing:.5px}
.f-title.small{font-size:21px}
.f-text{position:absolute;font-size:14px;line-height:18px}
.f-links{position:absolute;list-style:none;font-size:14px;line-height:27.5px}
.search{position:absolute;left:453px;top:233px;width:189px;height:37px;border:1.5px solid #fff;border-radius:19px;font-size:14px;line-height:34px;padding-left:14px}
</style>
</head>
<body>

<div class="card" style="top:0;height:49px"></div>

<!-- Step 2 -->
<section class="card" style="top:220px;height:1253px">
  <div class="band" style="height:171px"></div>
  <div class="badge orange" style="left:68px;top:-18px"><div class="step">STEP</div><div class="num">No.2</div></div>
  <h2 class="band-title" style="left:326px;top:36px">CHOOSE YOUR TOPICS</h2>
  <p class="band-sub" style="left:352px;top:88px;width:560px">SELECT THE TOPICS AND THE SPECFIY THE COURSE LENGTH</p>
  <p class="body-text" style="left:80px;top:227px;width:815px">TOVENQUARD comes with +250 out of the box awareness trainings for end users. All courses can be customized - or we can create your individual courses from scratch. Use the standard trainings or create a custom version.</p>
  <h2 class="sec-title" style="left:80px;top:326px">EXPLOR A FEW DESIGN TYPES</h2>

  <div class="type-card" style="left:82px"><h3>STANDARD TRAINING</h3>
    <div class="type-visual" role="img" aria-label="Illustration: computer monitor showing a training screen"></div></div>
  <div class="type-card" style="left:357px"><h3>CUSTOMIZED TRAINING</h3>
    <div class="type-visual" role="img" aria-label="Illustration: computer monitor showing a training screen"></div></div>
  <div class="type-card raised" style="left:633px"><h3>INDIVIDUAL TRAINING</h3>
    <div class="type-visual" role="img" aria-label="Illustration: computer monitor showing a training screen"></div></div>

  <ul class="topic-list" style="left:82px">
    <li>PCI Security</li><li>WLAN Security</li><li>Social Engineering</li><li>Clear Desk Policy</li><li>Data Privacy</li>
    <li>PCI Security</li><li>WLAN Security</li><li>Social Engineering</li><li>Clear Desk Policy</li><li>Data Privacy</li>
    <li>PCI Security</li><li>WLAN Security</li><li>Social Engineering</li><li>Clear Desk Policy</li><li>Data Privacy</li>
  </ul>
  <ul class="topic-list" style="left:357px">
    <li>Secure Social Networks</li><li>Secure Browsing</li><li>Phising</li><li>Password Security</li><li>Pysical Security</li>
    <li>Secure Social Networks</li><li>Secure Browsing</li><li>Phising</li><li>Password Security</li><li>Pysical Security</li>
    <li>Secure Social Networks</li><li>Secure Browsing</li><li>Phising</li><li>Password Security</li><li>Pysical Security</li>
  </ul>
  <ul class="topic-list" style="left:633px;padding-top:23px">
    <li>Shoulder Surfing</li><li>Malware</li><li>Traveling</li><li>Visitors</li><li>Spear Phising etc.</li>
    <li>Shoulder Surfing</li><li>Malware</li><li>Traveling</li><li>Visitors</li><li>Spear Phising etc.</li>
    <li>Shoulder Surfing</li><li>Malware</li><li>Traveling</li><li>Visitors</li><li>Spear Phising etc.</li>
  </ul>
</section>

<!-- Step 3 -->
<section class="card" style="top:1643px;height:1688px">
  <div class="band" style="height:173px;background:linear-gradient(100deg,#0c2a3e 0%,#123a52 55%,#0c2a3e 100%)"></div>
  <div class="badge teal" style="left:68px;top:-18px"><div class="step">STEP</div><div class="num">No.3</div></div>
  <h2 class="band-title" style="left:326px;top:38px">CUSTOMIZE!</h2>
  <p class="band-sub" style="left:352px;top:90px;width:480px">DESIGN IS MORE THAN JUST LAYOUT - IT IS ABOUT THE DESIRED USER EXPERIENCE</p>
  <p class="body-text" style="left:80px;top:218px;width:820px">Your might ask yourself why it needs customization? Beside just adjusting the design (logo, font, colours) to your corporate look and feel, it is important that the users perceives the training as something they can really relate. Examples:</p>

  <h2 class="sec-title" style="left:80px;top:308px">FROM CEO:</h2>
  <p class="body-text" style="left:80px;top:349px;width:395px">Add a personal greeting note from your CEO at the start of the training to highlight the importance of the training</p>
  <div class="photo" role="img" aria-label="Photo: executive and colleague in a meeting at a table by a brick wall" style="top:307px;background:linear-gradient(120deg,#b0603f 0%,#c9896b 45%,#e7e0d6 100%)"></div>

  <h2 class="sec-title" style="left:80px;top:675px">DO YOU KNOW OUR POLICIES?</h2>
  <p class="body-text" style="left:80px;top:716px;width:420px">You could ask your user to read and acknowledge your internal policies prior to starting the course</p>
  <div class="photo" role="img" aria-label="Photo: hands typing on a laptop showing a dashboard" style="top:674px;background:linear-gradient(135deg,#4a3a30 0%,#8a7a6c 50%,#d8d4cf 100%)"></div>

  <h2 class="sec-title" style="left:80px;top:987px">GET THE MESSAGE RIGHT!</h2>
  <p class="body-text" style="left:80px;top:1030px;width:820px">Probably you can use 90 % of the course out of the box. But certain chapters will need to be aligned with your policies or risks. In a password security course you want to tell the user&nbsp; the correct tips in regard password length. In a course about malware you won't need to warn a user to not plugin an unknown USB device, if the USB port is anyway blocked.</p>

  <h2 class="sec-title" style="left:80px;top:1173px">GET THE MESSAGE RIGHT!</h2>
  <div role="img" aria-label="Illustration: browser windows showing a password length tip and a padlock" style="position:absolute;left:192px;top:1247px;width:574px;height:328px;background:linear-gradient(180deg,#f4f6f8 0%,#e6ecf2 60%,#cfe7fb 100%);border-radius:6px"></div>
</section>

<!-- Step 4 -->
<section class="card" style="top:3436px;height:198px">
  <div class="badge grey" style="left:77px;top:-21px;width:141px"><div class="step">STEP</div><div class="num">No.4</div></div>
  <h2 class="band-title" style="left:297px;top:44px;font-size:31px">EXPORT (SCORM)</h2>
  <p class="body-text" style="left:297px;top:111px">Your file is complete and ready for the download</p>
  <div class="download">
    <svg width="52" height="44" viewBox="0 0 52 44"><path d="M2 6h16l5 5h27v31H2z" fill="#2aa3f5"/><path d="M2 14h48v28H2z" fill="#4cb8ff"/></svg>
    <span>Download</span>
  </div>
</section>

<!-- Footer -->
<footer class="footer">
  <h2 class="f-title" style="left:97px;top:184px">CONTACTS</h2>
  <p class="f-text" style="left:97px;top:230px">Address Europe<br>Tovenquard Security AG<br>Lindenweg 12 | 8040 Altbrugg | Switzerland</p>
  <p class="f-text" style="left:97px;top:326px">Address: North America<br>TOVENQUARD Security USA<br>4210 Meadowline Ave</p>

  <h2 class="f-title" style="left:453px;top:184px">SEARCH</h2>
  <div class="search">Search</div>
  <h2 class="f-title" style="left:453px;top:306px">CONNECT</h2>
  <div class="abs" style="left:453px;top:352px;width:32px;height:32px;border-radius:50%;background:#3f5c9a"></div>
  <span class="f-text" style="left:501px;top:359px">Friendwall</span>

  <h2 class="f-title small" style="left:737px;top:182px">INFORMATION</h2>
  <ul class="f-links" style="left:737px;top:216px">
    <li>Home</li><li>Solution</li><li>Pricing</li><li>Resources</li><li>About us</li><li>Support Wiki</li>
  </ul>

  <h2 class="f-title small" style="left:983px;top:182px">LANGUAGE</h2>
  <span class="f-text" style="left:983px;top:221px">English</span>
  <svg class="abs" style="left:1086px;top:226px" width="14" height="8" viewBox="0 0 14 8"><path d="M0 0h14L7 8z" fill="#fff"/></svg>
</footer>

</body>
</html>
```